NimbusFern cyber security firm Website

We did our website ourselves on Joomla, it's not great. We want a wordpress based redesign. Some thing that will represent a modern cyber security firm that's aimed at solving business problems.
Https://nimbusfern.co.nz (current site)
#58427c - primary color (you'll know why when you see it's name)
Logo files can be provided. Ask for more info if you need.

We want a modern, quick to load website. Website is going to have a home - services - products - about us - blogs menu. Will need a footer menu, site map, contact page etc.
We getting Content done sperately.
Our logo is #58427c - so hoping for a light theme (or at least the top is).
While we have been specific around the color - we are not after a website that has too much of it.

Reference sites that we like :
https://www.voltaline.co.nz/ - Love the full screen real world image
https://wardvex.co.nz/ (love the real world imagry and motion)
https://www.qtr.com/us-en?lnk=m
https://redowlen.com

Please dont use :
cartoon or redered images : (Like this : https://img.stockmorra.com/free-vector/cyber-security-concept_23-2148543851.jpg?w=2000 )

Please don't use images like this : https://www.tavelundi.com/eu/blog/oil-gas/app/uploads/2020/04/116137226_s-1440x564_c.jpg - they are old and boring.

We would like to see some creativity - loading our logo into a readymade wordpress template and hitting go won't cut it.
Updates

Thanks everyone who has submitted so far. We've extended the deadline as we wanted to give everyone a chance to Re- read the brief and perhaps make some tweeks should they feel it necessary.

Target Market(s)

Mid - large enterprise, finance, insurance, utilities vertical

Industry/Entity Type

Cyber security

Coding

Coded - Design and coding required

Number of Pages Required

5+ page

Font styles to use
Other font styles liked:
• Open sans

Colors

Designer to choose colors to be used in the design.

Requirements
Must have
• Simple clear messaging, something that catches user engagement
Nice to have
• Motion of some sort, but not overdone, GDPR

```html
<!DOCTYPE html>
<html lang="en">
<head>
<meta charset="utf-8">
<title>NimbusFern — Cyber Security</title>
<link href="https://fonts.googleapis.com/css2?family=Open+Sans:wght@400;600;700&family=Montserrat:wght@400;500;600;700&display=swap" rel="stylesheet">
<style>
:root{
  --primary:#58427c;
  --primary-dark:#3d2b63;
  --ink:#2a2438;
  --text:#4a4458;
  --muted:#7b7590;
  --tint:#ecebf2;
  --footer:#f8f7fb;
  --white:#ffffff;
  --hero-a:#2b2a8f;
  --hero-b:#1b1760;
  --hero-c:#3a2d86;
}
*{margin:0;padding:0;box-sizing:border-box}
html,body{width:1200px;height:3669px;overflow:hidden}
body{position:relative;background:var(--white);font-family:'Open Sans',sans-serif;color:var(--text)}
.abs{position:absolute}

/* Header */
.site-header{position:absolute;left:0;top:0;width:1200px;height:75px;background:var(--white)}
.brand{position:absolute;left:137px;top:18px;display:flex;align-items:center;gap:10px;font-family:'Open Sans',sans-serif;font-weight:600;font-size:27px;color:var(--primary);letter-spacing:.5px}
.brand-dot{width:30px;height:30px;border-radius:50%;background:var(--primary)}
.main-nav a{position:absolute;top:26px;font-size:13.5px;color:var(--ink);text-decoration:none;letter-spacing:.2px}
.main-nav a.active{color:var(--primary);font-weight:600}
.main-nav a.active::after{content:"";position:absolute;left:0;right:0;top:24px;height:2px;background:var(--primary)}

/* Hero */
.hero{position:absolute;left:0;top:75px;width:1200px;height:591px;background:linear-gradient(110deg,var(--hero-a) 0%,var(--hero-c) 45%,var(--hero-b) 100%)}
.hero-title{position:absolute;left:171px;top:178px;font-size:55px;line-height:60px;color:var(--white);font-weight:400;letter-spacing:.5px}
.hero-title strong{font-weight:700;display:block}
.hero-sub{position:absolute;left:174px;top:300px;font-size:16px;line-height:22px;color:var(--white);width:420px}
.btn{display:flex;align-items:center;justify-content:center;gap:10px;border-radius:24px;text-decoration:none;font-size:14px;letter-spacing:.3px}
.hero-btn{position:absolute;left:175px;top:371px;width:142px;height:34px;background:var(--white);color:var(--primary);font-size:11.5px}
.hero-dots{position:absolute;left:564px;top:536px;display:flex;gap:8px}
.hero-dots span{width:14px;height:14px;border-radius:50%;background:var(--white)}
.hero-dots span:first-child{background:transparent;border:2px solid var(--white)}

/* Services */
.service-card{position:absolute;top:740px;width:310px;height:330px}
.service-card svg.shape{position:absolute;left:0;top:0}
.service-icon{position:absolute;left:119px;top:43px}
.service-title{position:absolute;left:0;width:100%;top:126px;text-align:center;font-size:22px;color:var(--ink)}
.service-text{position:absolute;left:65px;width:180px;top:163px;text-align:center;font-size:12.5px;line-height:20px;color:var(--text)}
.service-link{position:absolute;left:0;width:100%;top:254px;text-align:center;font-size:11px;color:var(--primary)}

/* About */
.about{position:absolute;left:0;top:1167px;width:1200px;height:632px;background:var(--tint)}
.section-title{position:absolute;width:100%;text-align:center;font-size:41px;color:var(--primary);font-weight:400;letter-spacing:.5px}
.section-title b{font-weight:700}
.title-rule{position:absolute;height:2px;width:94px;background:var(--primary)}
.title-rule::after{content:"";position:absolute;left:50%;top:-5px;margin-left:-5px;border:5px solid transparent;border-top:0;border-bottom:5px solid var(--primary)}
.about-mark{position:absolute;left:180px;top:210px;width:360px;height:360px;border-radius:50%;background:radial-gradient(circle,#d9d5e6 0%,var(--tint) 70%)}
.about-mark span{position:absolute;left:0;width:100%;top:160px;text-align:center;font-size:40px;font-weight:600;color:var(--primary)}
.about-copy{position:absolute;left:620px;top:198px;width:450px;font-size:15px;line-height:20.5px;color:var(--text)}
.about-copy p{margin-bottom:20px}
.about-copy strong{color:var(--ink);font-weight:600}
.btn-solid{background:var(--primary);color:var(--white);font-family:'Montserrat',sans-serif;font-weight:500}

/* Blogs */
.blog-feature{position:absolute;left:154px;top:1993px;width:548px;height:363px;background:linear-gradient(120deg,#1f3c5e 0%,#2c5f8a 45%,#152a46 100%)}
.blog-item{position:absolute;left:720px;width:360px;height:108px}
.blog-thumb{position:absolute;left:0;top:0;width:164px;height:108px;background:linear-gradient(135deg,#163b5c,#2d6f9a 60%,#0f2740)}
.blog-cat{position:absolute;left:178px;top:0;font-family:'Montserrat',sans-serif;font-size:11px;color:var(--primary);font-weight:500}
.blog-title{position:absolute;left:178px;top:20px;width:190px;font-family:'Montserrat',sans-serif;font-size:15.5px;line-height:22px;font-weight:700;color:var(--ink)}
.blog-date{position:absolute;left:178px;top:91px;font-family:'Montserrat',sans-serif;font-size:9.5px;color:var(--ink)}

/* Contact */
.contact{position:absolute;left:0;top:2548px;width:1200px;height:695px;background:var(--tint)}
.contact-title{position:absolute;left:135px;top:144px;font-family:'Montserrat',sans-serif;font-size:40px;color:var(--primary);font-weight:400}
.contact-title b{font-weight:700}
.contact-item{position:absolute;left:132px;display:flex;align-items:center;gap:16px;font-family:'Montserrat',sans-serif;font-size:17px;line-height:29px;color:var(--muted)}
.icon-badge{width:52px;height:52px;border-radius:50%;background:var(--primary);display:flex;align-items:center;justify-content:center;flex:none}
.contact-form{position:absolute;left:605px;top:73px;width:436px;height:549px;background:var(--primary)}
.field{position:absolute;left:46px;width:336px;height:54px;background:var(--white);font-family:'Montserrat',sans-serif;font-size:16px;color:var(--primary);padding:17px 14px}
.submit{position:absolute;left:48px;top:467px;width:148px;height:37px;border:2px solid var(--white);color:var(--white);font-family:'Montserrat',sans-serif;font-size:14px;font-weight:700;display:flex;align-items:center;justify-content:center}

/* Footer */
.site-footer{position:absolute;left:0;top:3243px;width:1200px;height:426px;background:var(--footer)}
.footer-brand{position:absolute;left:140px;top:150px;width:236px;text-align:center;font-size:30px;font-weight:600;color:var(--primary)}
.socials{position:absolute;left:193px;top:212px;display:flex;gap:15px}
.socials span{width:32px;height:32px;border-radius:50%;background:var(--primary)}
.footer-sep{position:absolute;top:50px;width:1px;height:160px;background:#e2dfea}
.footer-col{position:absolute;font-family:'Montserrat',sans-serif}
.footer-col h4{font-size:15px;color:var(--primary);font-weight:700;border-left:3px solid var(--primary);padding-left:16px;margin-left:-19px;margin-bottom:12px;line-height:22px}
.footer-col a{display:block;font-size:14px;color:var(--muted);text-decoration:none;line-height:29px}
.footer-col.small h4{font-size:13px}
.info-row{position:absolute;left:883px;display:flex;align-items:center;gap:10px;font-family:'Montserrat',sans-serif;font-size:11px;line-height:13px;color:var(--muted)}
.info-row .icon-badge{width:32px;height:32px}
.footer-bottom{position:absolute;left:0;top:358px;width:1200px;height:68px;border-top:1px solid #dcd8e6;text-align:center;padding-top:20px;font-size:10.5px;color:var(--muted)}
</style>
</head>
<body>

<header class="site-header">
  <div class="brand"><span class="brand-dot"></span>NIMBUSFERN</div>
  <nav class="main-nav">
    <a href="#" class="active" style="left:546px">HOME</a>
    <a href="#" style="left:619px">SERVICES ⌄</a>
    <a href="#" style="left:719px">PRODUCTS</a>
    <a href="#" style="left:820px">ABOUT US</a>
    <a href="#" style="left:920px">BLOGS</a>
    <a href="#" style="left:993px">CONTACT US</a>
  </nav>
</header>

<section class="hero" role="img" aria-label="Security operations centre with analysts working at rows of monitors">
  <h1 class="hero-title">HUMAN RISK<strong>MANAGEMENT</strong></h1>
  <p class="hero-sub">Calculate, reduce and monitor human cyber risk with the new-class of user-focused security.</p>
  <a href="#" class="btn hero-btn">LEARN MORE
    <svg width="16" height="14" viewBox="0 0 16 14"><path d="M2 4a9 9 0 0 1 12 0M4 7a6 6 0 0 1 8 0M6 10a3 3 0 0 1 4 0" fill="none" stroke="#58427c" stroke-width="1.6" stroke-linecap="round"/></svg>
  </a>
  <div class="hero-dots"><span></span><span></span><span></span><span></span></div>
</section>

<!-- Services -->
<svg width="0" height="0" style="position:absolute">
  <defs>
    <filter id="soft" x="-20%" y="-20%" width="140%" height="140%"><feDropShadow dx="0" dy="4" stdDeviation="8" flood-color="#58427c" flood-opacity=".12"/></filter>
  </defs>
</svg>

<article class="service-card" style="left:125px">
  <svg class="shape" width="310" height="330" viewBox="0 0 310 330"><path d="M155 14C215 14 265 26 294 44C294 165 252 255 155 316C58 255 16 165 16 44C45 26 95 14 155 14Z" fill="#fff" stroke="#f1eff6" stroke-width="6" filter="url(#soft)"/></svg>
  <svg class="service-icon" width="72" height="76" viewBox="0 0 72 76"><path d="M36 2L68 12C68 44 56 62 36 74C16 62 4 44 4 12Z" fill="#58427c"/><rect x="28" y="34" width="16" height="13" rx="2" fill="none" stroke="#fff" stroke-width="2"/><path d="M31 34v-4a5 5 0 0 1 10 0v4" fill="none" stroke="#fff" stroke-width="2"/></svg>
  <h3 class="service-title">VIRTUAL CISO</h3>
  <p class="service-text">The vCISO is a security practi-tioner who uses the culmina-tion of their years of cyberse-curity</p>
  <a class="service-link">LEARN MORE &nbsp;→</a>
</article>

<article class="service-card" style="left:440px">
  <svg class="shape" width="310" height="330" viewBox="0 0 310 330"><path d="M155 14C215 14 265 26 294 44C294 165 252 255 155 316C58 255 16 165 16 44C45 26 95 14 155 14Z" fill="#fff" stroke="#f1eff6" stroke-width="6" filter="url(#soft)"/></svg>
  <svg class="service-icon" width="72" height="76" viewBox="0 0 72 76"><path d="M36 2L68 12C68 44 56 62 36 74C16 62 4 44 4 12Z" fill="#58427c"/><circle cx="36" cy="38" r="9" fill="none" stroke="#fff" stroke-width="2"/><path d="M24 30l6 4M48 30l-6 4M24 46l6-3M48 46l-6-3" stroke="#fff" stroke-width="2"/></svg>
  <h3 class="service-title">CYBER THREAT</h3>
  <p class="service-text">A cyber threat susceptibility assessment is something every business should do. Our pragmatic 3 step assess-</p>
  <a class="service-link">LEARN MORE &nbsp;→</a>
</article>

<article class="service-card" style="left:757px">
  <svg class="shape" width="310" height="330" viewBox="0 0 310 330"><path d="M155 14C215 14 265 26 294 44C294 165 252 255 155 316C58 255 16 165 16 44C45 26 95 14 155 14Z" fill="#fff" stroke="#f1eff6" stroke-width="6" filter="url(#soft)"/></svg>
  <svg class="service-icon" width="72" height="76" viewBox="0 0 72 76"><path d="M36 2L68 12C68 44 56 62 36 74C16 62 4 44 4 12Z" fill="#58427c"/><rect x="24" y="26" width="24" height="17" rx="1.5" fill="none" stroke="#fff" stroke-width="2"/><path d="M20 48h32" stroke="#fff" stroke-width="2"/></svg>
  <h3 class="service-title">CYBER RISK</h3>
  <p class="service-text">NimbusFern's Third Party Risk Management service is based on the Redowlen platform. As one of the most</p>
  <a class="service-link">LEARN MORE &nbsp;→</a>
</article>

<!-- About -->
<section class="about">
  <h2 class="section-title" style="top:60px"><b>ABOUT</b> US</h2>
  <div class="title-rule" style="left:553px;top:131px"></div>
  <div class="about-mark"><span>NimbusFern</span></div>
  <div class="about-copy">
    <p><strong>NimbusFern is a 100% New Zealand owned and operated cyber security company, providing cyber risk mitigation and management solutions to all businesses.</strong> We pride our-selves in delivering enterprise grade security solutions, to businesses of all sizes and industries, in Aotearoa.</p>
    <p>Being 'purple' we focus on both Blue and Red team security solutions, assisting our clients in implementing new security controls, as well as testing the ones they already have.</p>
    <p>Our key value is integrity, and we believe in being fully trans-parent when working with our clients and partners to ensure we achieve the best possible security solutions for the best price.</p>
  </div>
  <a href="#" class="btn btn-solid abs" style="left:618px;top:503px;width:174px;height:43px">LEARN MORE
    <svg width="18" height="16" viewBox="0 0 16 14"><path d="M2 4a9 9 0 0 1 12 0M4 7a6 6 0 0 1 8 0M6 10a3 3 0 0 1 4 0" fill="none" stroke="#fff" stroke-width="1.6" stroke-linecap="round"/></svg>
  </a>
</section>

<!-- Blogs -->
<h2 class="section-title" style="top:1878px">LATEST <b>BLOGS</b></h2>
<div class="title-rule" style="left:553px;top:1946px"></div>
<div class="blog-feature" role="img" aria-label="Engineer working at a multi-screen workstation in a dark office"></div>

<article class="blog-item" style="top:1993px">
  <div class="blog-thumb" role="img" aria-label="Analyst at a desk surrounded by monitors"></div>
  <span class="blog-cat">CYBER SECURITY</span>
  <h3 class="blog-title">Lorem ipsum dolor sit amet, consectetur adipiscing</h3>
  <span class="blog-date">28 Feb 2022</span>
</article>
<article class="blog-item" style="top:2120px">
  <div class="blog-thumb" role="img" aria-label="Dark digital code backdrop"></div>
  <span class="blog-cat">CYBER SECURITY</span>
  <h3 class="blog-title">Lorem ipsum dolor sit amet, consectetur adipiscing</h3>
  <span class="blog-date">28 Feb 2022</span>
</article>
<article class="blog-item" style="top:2248px">
  <div class="blog-thumb" role="img" aria-label="Blue-lit data centre dashboards"></div>
  <span class="blog-cat">CYBER SECURITY</span>
  <h3 class="blog-title">Lorem ipsum dolor sit amet, consectetur adipiscing</h3>
  <span class="blog-date">28 Feb 2022</span>
</article>

<a href="#" class="btn btn-solid abs" style="left:512px;top:2401px;width:176px;height:43px">LEARN MORE
  <svg width="18" height="16" viewBox="0 0 16 14"><path d="M2 4a9 9 0 0 1 12 0M4 7a6 6 0 0 1 8 0M6 10a3 3 0 0 1 4 0" fill="none" stroke="#fff" stroke-width="1.6" stroke-linecap="round"/></svg>
</a>

<!-- Contact -->
<section class="contact">
  <h2 class="contact-title"><b>CONTACT</b> US</h2>
  <div class="title-rule" style="left:135px;top:209px"></div>

  <div class="contact-item" style="top:259px">
    <span class="icon-badge"><svg width="20" height="26" viewBox="0 0 20 26"><path d="M10 1a9 9 0 0 0-9 9c0 7 9 15 9 15s9-8 9-15a9 9 0 0 0-9-9z" fill="#fff"/><circle cx="10" cy="10" r="3.5" fill="#58427c"/></svg></span>
    <span>52b Kereru Lane, Tawhiti,<br>Port Alder, 4391</span>
  </div>
  <div class="contact-item" style="top:352px">
    <span class="icon-badge"><svg width="24" height="24" viewBox="0 0 24 24"><rect x="2" y="4" width="18" height="16" rx="2" fill="none" stroke="#fff" stroke-width="1.8"/><path d="M2 9h18M7 2v4M15 2v4" stroke="#fff" stroke-width="1.8"/><circle cx="17" cy="17" r="5" fill="#58427c" stroke="#fff" stroke-width="1.6"/></svg></span>
    <span>Monday-Friday<br>08:00 - 18:00</span>
  </div>
  <div class="contact-item" style="top:450px">
    <span class="icon-badge"><svg width="24" height="24" viewBox="0 0 24 24"><rect x="2" y="4" width="18" height="16" rx="2" fill="none" stroke="#fff" stroke-width="1.8"/><path d="M2 9h18M7 2v4M15 2v4" stroke="#fff" stroke-width="1.8"/><circle cx="17" cy="17" r="5" fill="#58427c" stroke="#fff" stroke-width="1.6"/></svg></span>
    <span>Saturday-Sunday<br>18:00 - 22:00</span>
  </div>

  <form class="contact-form">
    <div class="field" style="top:45px">First name*</div>
    <div class="field" style="top:108px">Last name</div>
    <div class="field" style="top:169px">Phone*</div>
    <div class="field" style="top:232px">Email address*</div>
    <div class="field" style="top:293px;height:155px">Message</div>
    <div class="submit">SUBMIT NOW</div>
  </form>
</section>

<!-- Footer -->
<footer class="site-footer">
  <div class="footer-brand">NIMBUSFERN</div>
  <div class="socials"><span></span><span></span><span></span></div>
  <div class="footer-sep" style="left:410px"></div>
  <div class="footer-sep" style="left:649px"></div>
  <div class="footer-sep" style="left:857px"></div>

  <nav class="footer-col" style="left:431px;top:96px">
    <h4>Navigation</h4>
    <a>Home</a><a>About us</a><a>products</a><a>Our Services</a><a>Blogs</a><a>Contact us</a>
  </nav>
  <nav class="footer-col small" style="left:665px;top:96px">
    <h4>Other Links</h4>
    <a>Terms &amp; Conditions</a><a>Prvacy Policy</a>
  </nav>
  <div class="footer-col small" style="left:883px;top:97px"><h4>Contact Information</h4></div>

  <div class="info-row" style="top:126px">
    <span class="icon-badge"><svg width="12" height="16" viewBox="0 0 20 26"><path d="M10 1a9 9 0 0 0-9 9c0 7 9 15 9 15s9-8 9-15a9 9 0 0 0-9-9z" fill="#fff"/></svg></span>
    <span>52b Kereru Lane, Tawhiti,<br>Port Alder, 4391</span>
  </div>
  <div class="info-row" style="top:169px">
    <span class="icon-badge"><svg width="14" height="14" viewBox="0 0 24 24"><path d="M6 2l4 5-2 3a12 12 0 0 0 6 6l3-2 5 4-2 4C10 22 2 14 2 4z" fill="#fff"/></svg></span>
    <span>+64 (0) 210 555 0142</span>
  </div>
  <div class="info-row" style="top:214px">
    <span class="icon-badge"><svg width="14" height="11" viewBox="0 0 20 14"><rect x="1" y="1" width="18" height="12" fill="none" stroke="#fff" stroke-width="1.8"/><path d="M1 1l9 7 9-7" fill="none" stroke="#fff" stroke-width="1.8"/></svg></span>
    <span>info@nimbusfern.co.nz</span>
  </div>

  <div class="footer-bottom">© 2022 NIMBUSFERN LTD. ALL RIGHT RESERVED</div>
</footer>

</body>
</html>
```